Pipelining Product Supply Company Needs New Stationery

We need new stationery (letter head, with compliments slips & business card) for our industry leading pipe lining supply company. basically we sell product to other plumbers to carry out pipe relining.

Im looking for something, fresh, professional, sleek and modern at the same time.

Ive attached a copy of the logo and also some guidelines to follow for colours and fonts etc.

Target Market(s)

Plumbers

Industry/Entity Type

Plumbing

Font styles to use
Sans Serif

Requirements
Must have
• The logo, space for ABN, Address, Phone Number, website and email.
Nice to have
• Stand out from the crowd. To look sleep and professional.
Should not have
• Any other colours apart from what is on the guidelines.

```html
<!DOCTYPE html>
<html lang="en">
<head>
<meta charset="utf-8">
<title>Kestrel Pipe Supply — Stationery</title>
<link href="https://fonts.googleapis.com/css2?family=Work+Sans:wght@400;600;700&display=swap" rel="stylesheet">
<style>
  :root {
    --green: #7cc242;
    --dark: #231f20;
    --text: #7a7a7a;
    --text-dark: #4a4a4a;
    --paper: #ffffff;
    --backdrop: #e9e9e9;
    --shadow: 0 2px 8px rgba(0,0,0,.22);
  }
  * { box-sizing: border-box; margin: 0; padding: 0; }
  html, body { width: 1200px; height: 825px; overflow: hidden; }
  body {
    background: var(--backdrop);
    font-family: "Work Sans", Arial, sans-serif;
    color: var(--text);
    position: relative;
  }
  .sheet { position: absolute; background: var(--paper); box-shadow: var(--shadow); overflow: hidden; }

  .brand { position: absolute; display: flex; align-items: center; gap: 8px; }
  .brand-mark { background: var(--green); flex: none; }
  .brand-name { color: var(--green); font-weight: 700; line-height: 1.05; letter-spacing: .01em; }

  .band { position: absolute; left: 0; bottom: 0; width: 100%; display: block; }

  /* Letterhead */
  .letterhead { left: 54px; top: 43px; width: 512px; height: 723px; }
  .letterhead .brand { left: 34px; top: 42px; }
  .letterhead .brand-mark { width: 30px; height: 30px; }
  .letterhead .brand-name { font-size: 27px; }
  .salutation { position: absolute; left: 34px; top: 216px; font-size: 14px; }
  .letter-body { position: absolute; left: 34px; top: 262px; width: 446px; font-size: 9.4px; line-height: 13.5px; }
  .letter-body p { margin-bottom: 15px; }
  .signature { position: absolute; left: 34px; top: 505px; width: 150px; height: 28px; background: #efefef; border-radius: 3px; }
  .rule { position: absolute; left: 34px; top: 622px; width: 444px; height: 1.5px; background: var(--green); }
  .contacts { position: absolute; list-style: none; font-size: 12px; line-height: 16px; }
  .contacts li { display: flex; align-items: center; gap: 8px; }
  .contacts svg { width: 7px; height: 7px; fill: var(--green); flex: none; }
  .letterhead .contacts { left: 34px; top: 643px; }
  .address { position: absolute; text-align: right; font-size: 12px; line-height: 16px; }
  .letterhead .address { right: 34px; top: 659px; }

  /* Business card */
  .card { top: 44px; width: 246px; height: 140px; }
  .card-front { left: 636px; }
  .card-front .brand { left: 14px; top: 52px; gap: 5px; }
  .card-front .brand-mark { width: 12px; height: 12px; }
  .card-front .brand-name { font-size: 11.5px; }
  .card-divider { position: absolute; left: 131px; top: 38px; width: 1px; height: 62px; background: var(--green); }
  .card-details { position: absolute; left: 147px; top: 37px; color: var(--dark); font-size: 5.6px; line-height: 7.6px; }
  .card-name { color: var(--green); font-weight: 700; font-size: 9.5px; line-height: 11px; }
  .card-role { margin-bottom: 4px; }
  .card-addr { margin-bottom: 3px; }
  .card-details .contacts { position: static; font-size: 5.6px; line-height: 7.6px; }
  .card-details .contacts li { gap: 3px; }
  .card-details .contacts svg { width: 3px; height: 3px; }
  .card-back { left: 896px; background: var(--dark); }
  .card-back .brand { left: 0; right: 0; top: 58px; justify-content: center; }
  .card-back .brand-mark { width: 16px; height: 16px; }
  .card-back .brand-name { font-size: 17px; }

  /* Envelope */
  .envelope { left: 636px; top: 225px; width: 506px; height: 253px; }
  .flap { position: absolute; left: 0; top: 0; width: 100%; height: 76px; background: var(--dark); border-radius: 0 0 26px 26px / 0 0 20px 20px; margin: 0; }
  .flap-wrap { position: absolute; left: 8px; right: 8px; top: 0; height: 76px; }
  .envelope .brand { left: 0; right: 0; top: 24px; justify-content: center; }
  .envelope .brand-mark { width: 13px; height: 13px; }
  .envelope .brand-name { font-size: 14px; }

  /* Compliments slip */
  .slip { left: 636px; top: 516px; width: 506px; height: 254px; }
  .slip .brand { left: 19px; top: 44px; }
  .slip .brand-mark { width: 24px; height: 24px; }
  .slip .brand-name { font-size: 22px; }
  .slip .contacts { left: 19px; top: 186px; font-size: 11.5px; line-height: 15px; }
  .slip .address { right: 19px; top: 201px; font-size: 11.5px; line-height: 15px; }
</style>
</head>
<body>

<section class="sheet letterhead">
  <div class="brand"><span class="brand-mark"></span><span class="brand-name">Kestrel Pipe Supply</span></div>
  <p class="salutation">Dear sir,</p>
  <div class="letter-body">
    <p>Lorem ipsum dolor sit amet, an vel recteque dissentiet, detracto albucius platonem ex vel, eros repudiandae cu. Atqui aliquando nec an, unum graece adolescens vel ad. Id odio scae has, iudico euismod atomorum ius ea, cum ea honestatis quaerendum theophrastus. Mea honestatis quaerendum theophrastus. Mea</p>
    <p>Lorem ipsum dolor sit amet, an vel recteque dissentiet, detracto albucius platonem ex vel, eros repudiandae cu. Atqui aliquando nec an, unum graece adolescens vel ad. Id odio scae has, iudico euismod atomorum ius ea, cum ea honestatis quaerendum theophrastus. Mea doming repudiandae ex, cu cum civibus assentior posidonium. Quo etiam pertinax ex, te eros repudiandae cu. Atqui aliquando nec an, unum graece adolescens vel ad. Id odio scae honestatis quaerendum theophrastus. Mea</p>
    <p>eros repudiandae cu. Atqui aliquando nec an, unum graece adolescens vel ad. Id odio scae honestatis quaerendum theophrastus. Mea posidonium. Quo etiam pertinax ex, te etiam pertinax ex, te</p>
  </div>
  <div class="signature" role="img" aria-label="Handwritten signature of Daniel Reyes"></div>
  <div class="rule"></div>
  <ul class="contacts">
    <li><svg viewBox="0 0 8 8"><path d="M1 0h2l1 2-1 1a5 5 0 0 0 2 2l1-1 2 1v2a1 1 0 0 1-1 1A7 7 0 0 1 0 1a1 1 0 0 1 1-1z"/></svg>555-014-2290</li>
    <li><svg viewBox="0 0 8 8"><rect x="0" y="1" width="8" height="6"/></svg>hello@kestrelpipe.com</li>
    <li><svg viewBox="0 0 8 8"><circle cx="4" cy="4" r="4"/></svg>www.kestrelpipe.com</li>
  </ul>
  <p class="address">48 Harbour Rd.<br>Lakeview, FL 33010</p>
  <svg class="band" viewBox="0 0 512 12" height="12" preserveAspectRatio="none"><polygon points="0,0 259,0 247,12 0,12" fill="var(--dark)"/><polygon points="266,0 512,0 512,12 254,12" fill="var(--green)"/></svg>
</section>

<section class="sheet card card-front">
  <div class="brand"><span class="brand-mark"></span><span class="brand-name">Kestrel Pipe<br>Supply</span></div>
  <div class="card-divider"></div>
  <div class="card-details">
    <p class="card-name">DANIEL REYES</p>
    <p class="card-role">Founder</p>
    <p class="card-addr">48 Harbour Rd.<br>Lakeview, FL 33010</p>
    <ul class="contacts">
      <li><svg viewBox="0 0 8 8"><circle cx="4" cy="4" r="4"/></svg>555-014-2290</li>
      <li><svg viewBox="0 0 8 8"><rect width="8" height="8"/></svg>hello@kestrelpipe.com</li>
      <li><svg viewBox="0 0 8 8"><circle cx="4" cy="4" r="4"/></svg>www.kestrelpipe.com</li>
    </ul>
  </div>
  <svg class="band" viewBox="0 0 246 8" height="8" preserveAspectRatio="none"><polygon points="0,0 126,0 118,8 0,8" fill="var(--dark)"/><polygon points="131,0 246,0 246,8 123,8" fill="var(--green)"/></svg>
</section>

<section class="sheet card card-back">
  <div class="brand"><span class="brand-mark"></span><span class="brand-name">Kestrel Pipe Supply</span></div>
</section>

<section class="sheet envelope">
  <div class="flap-wrap"><div class="flap"></div></div>
  <div class="brand"><span class="brand-mark"></span><span class="brand-name">Kestrel Pipe Supply</span></div>
</section>

<section class="sheet slip">
  <div class="brand"><span class="brand-mark"></span><span class="brand-name">Kestrel Pipe Supply</span></div>
  <ul class="contacts">
    <li><svg viewBox="0 0 8 8"><path d="M1 0h2l1 2-1 1a5 5 0 0 0 2 2l1-1 2 1v2a1 1 0 0 1-1 1A7 7 0 0 1 0 1a1 1 0 0 1 1-1z"/></svg>555-014-2290</li>
    <li><svg viewBox="0 0 8 8"><rect x="0" y="1" width="8" height="6"/></svg>hello@kestrelpipe.com</li>
    <li><svg viewBox="0 0 8 8"><circle cx="4" cy="4" r="4"/></svg>www.kestrelpipe.com</li>
  </ul>
  <p class="address">48 Harbour Rd.<br>Lakeview, FL 33010</p>
  <svg class="band" viewBox="0 0 506 12" height="12" preserveAspectRatio="none"><polygon points="0,0 255,0 243,12 0,12" fill="var(--dark)"/><polygon points="262,0 506,0 506,12 250,12" fill="var(--green)"/></svg>
</section>

</body>
</html>
```